Plakat für FBV Erlangen
Zielgruppe
Die FBV Erlangen ist der Kreisverband der Freien Bürgerlichen Vereinigung in Erlangen.
Aufgabenstellung
Es soll ein Plakat (DinA0, Hochformat) designed werden, welches als Basisplakat für verschiedene Veranstaltungen der FBV Erlangen dienen soll. Um dies zu gewährleisten, soll das Plakat eine zentrale freie Fläche mit einer hellen Hintergrundfarbe (z.B. weiß) besitzen, die groß genug ist, um ein ausgedrucktes DinA3 Papier mit Veranstaltungsinformationen darauf zu befestigen.
Das Basisplakat, welches sich an der CI der FBV orientieren soll, soll darüber hinaus das Logo des Kreisverbands Erlangen sowie den Slogan "Bei Ihnen. Direkt. Vor Ort" enthalten. Das FBV-Blau kann bei der Gestaltung des Plakats gerne als Hauptfarbe fungieren.
Ebenfalls enthalten sein soll der Vermerk im Sinne des Pressgesetzes: "VisdP: FBV Erlangen, Amselgrund-Str. 14b, 91047 Erlangen".
Die fertigen Datei soll auch in einem Format vorliegen, das mit Adobe Photoshop oder Illustrator geöffnet und bearbeitet werden kann.
Vielen herzlichen Dank schon mal für Ihre kreativen Entwürfe!

```html
<!DOCTYPE html>
<html lang="de">
<head>
<meta charset="utf-8">
<title>Basisplakat FBV Erlangen</title>
<link rel="stylesheet" href="https://fonts.googleapis.com/css2?family=Fira+Sans+Condensed:wght@700&family=Fira+Sans:wght@400&display=swap">
<style>
  :root {
    --fbv-blue: #0081c9;
    --fbv-green: #009d3c;
    --pattern-blue: #a6c9ec;
    --frame-grey: #b9b9b9;
    --footer-grey: #6a6a6a;
    --paper: #ffffff;
  }
  html, body {
    margin: 0;
    padding: 0;
    width: 1200px;
    height: 1200px;
    overflow: hidden;
    background: var(--paper);
  }
  .canvas {
    display: block;
    width: 1200px;
    height: 1200px;
  }
  .slogan {
    font-family: "Fira Sans Condensed", "Arial Narrow", sans-serif;
    font-weight: 700;
    fill: var(--paper);
  }
  .brand-name {
    font-family: "Fira Sans Condensed", "Arial Narrow", sans-serif;
    font-weight: 700;
    fill: var(--fbv-blue);
  }
  .imprint {
    font-family: "Fira Sans", Arial, sans-serif;
    font-weight: 400;
    fill: var(--footer-grey);
  }
</style>
</head>
<body>
<svg class="canvas" viewBox="0 0 1772 1772" xmlns="http://www.w3.org/2000/svg">
  <defs>
    <linearGradient id="pattern-fade" x1="0" x2="1" y1="0" y2="0">
      <stop offset="0" stop-color="var(--pattern-blue)" stop-opacity="0.9"/>
      <stop offset="0.55" stop-color="var(--pattern-blue)" stop-opacity="0.35"/>
      <stop offset="1" stop-color="var(--pattern-blue)" stop-opacity="0"/>
    </linearGradient>
    <filter id="sheet-shadow" x="-5%" y="-5%" width="112%" height="112%">
      <feDropShadow dx="2" dy="3" stdDeviation="2" flood-color="#000" flood-opacity="0.3"/>
    </filter>
  </defs>

  <g class="poster">
    <rect class="poster-sheet" x="343.5" y="125.5" width="1066" height="1508" fill="var(--paper)" stroke="var(--frame-grey)" stroke-width="1"/>

    <rect class="diamond-backdrop" x="344" y="126" width="360" height="1507" fill="url(#pattern-fade)" role="img" aria-label="Blau-weißes Rautenmuster, nach rechts ausblendend"/>

    <g class="slogan-bands">
      <rect class="band band-blue" x="400" y="190" width="610" height="150" fill="var(--fbv-blue)"/>
      <text class="slogan" x="440" y="305" font-size="104">Bei Ihnen.</text>

      <rect class="band band-green" x="735" y="366" width="600" height="136" fill="var(--fbv-green)"/>
      <text class="slogan" x="1300" y="472" font-size="104" text-anchor="end">Direkt.</text>

      <rect class="band band-green" x="700" y="527" width="600" height="136" fill="var(--fbv-green)"/>
      <text class="slogan" x="1265" y="633" font-size="104" text-anchor="end">Vor Ort.</text>
    </g>

    <rect class="event-sheet-area" x="685" y="719" width="376" height="531" fill="var(--paper)" filter="url(#sheet-shadow)"/>

    <g class="brand-mark">
      <text class="brand-name" x="1345" y="1440" font-size="96" text-anchor="end">FBV Erlangen</text>
    </g>

    <text class="imprint" x="390" y="1594" font-size="28" textLength="963" lengthAdjust="spacing">VisdP: FBV Erlangen, Amselgrund-Str. 14b, 91047 Erlangen</text>
  </g>
</svg>
</body>
</html>
```